Website banner

Here is the link where the current banner is featured https://www.brimlark.com.au/collections/gel-blasters

I need the banner recreated into desktop and mobile format size.
Update the key points to:
- FREE SHIPPING AUSTRALIA WIDE
- SAME DAY DISPATCH
- BEST PRICE GUARANTEE
- 3000+ 5 STAR REVIEWS
- BEST SERVICE & WARRANTY
- 100% SECURE CHECKOUT

I want the banner to suit the style of the website and make it look better than the last graphic.

I also need the "save even more" picture to be recreated as it looks very plain at the moment,

```html
<!DOCTYPE html>
<html lang="en">
<head>
<meta charset="utf-8">
<title>Brimlark Gel Blasters – Key Benefits Banner</title>
<link rel="stylesheet" href="https://fonts.googleapis.com/css2?family=Montserrat:wght@600&display=swap">
<style>
  :root {
    --page-bg: #ffffff;
    --band-black: #0c0c0c;
    --brand-red: #d01c24;
    --red-deep: #8e1016;
    --red-light: #ee2f3a;
    --cart-red: #9a1418;
    --text-white: #ffffff;
  }
  html, body {
    margin: 0;
    padding: 0;
    width: 1200px;
    height: 308px;
    overflow: hidden;
    background: var(--page-bg);
  }
  .banner {
    position: absolute;
    left: 21px;
    top: 29px;
    width: 1158px;
    height: 241px;
    background: var(--band-black);
    overflow: hidden;
  }
  .banner__art {
    position: absolute;
    left: -21px;
    top: -29px;
    width: 1200px;
    height: 308px;
  }
  .benefits {
    position: absolute;
    left: 0;
    top: 0;
    width: 1200px;
    height: 308px;
    margin: 0;
    padding: 0;
    list-style: none;
  }
  .benefit {
    position: absolute;
    top: 114px;
    width: 120px;
    margin-left: -60px;
    text-align: center;
    color: var(--text-white);
    font-family: "Montserrat", sans-serif;
    font-weight: 600;
    font-size: 11px;
    line-height: 13px;
    letter-spacing: 0.2px;
  }
  .benefit__icon {
    display: block;
    width: 50px;
    height: 50px;
    margin: 0 auto 7px;
  }
  .cart-button {
    position: absolute;
    left: 1067px;
    top: 199px;
    width: 58px;
    height: 58px;
    border-radius: 50%;
    background: var(--text-white);
    display: flex;
    align-items: center;
    justify-content: center;
  }
</style>
</head>
<body>
  <section class="banner" aria-label="Brimlark gel blasters benefits">
    <svg class="banner__art" viewBox="0 0 1200 308" role="img" aria-label="Red-tinted photograph of assorted gel blaster pistols and rifles on a peeled-back red sheet">
      <defs>
        <linearGradient id="sheetFill" x1="0" y1="0" x2="1" y2="1">
          <stop offset="0" stop-color="#c41a22"/>
          <stop offset="0.5" stop-color="#d21d26"/>
          <stop offset="1" stop-color="#a8151c"/>
        </linearGradient>
        <linearGradient id="flapLeft" x1="0" y1="0" x2="1" y2="0">
          <stop offset="0" stop-color="#f03440"/>
          <stop offset="1" stop-color="#9e1219"/>
        </linearGradient>
        <linearGradient id="flapRight" x1="1" y1="0" x2="0" y2="0">
          <stop offset="0" stop-color="#f03440"/>
          <stop offset="1" stop-color="#a8141b"/>
        </linearGradient>
      </defs>
      <path d="M303 29 L992 29 C1000 60 1010 90 1027 109 C960 150 920 220 883 270 L200 270 C180 240 172 215 170 191 C220 140 270 80 303 29 Z" fill="url(#sheetFill)"/>
      <path d="M303 29 C270 80 220 140 170 191 C175 200 180 205 186 200 C220 150 265 90 303 29 Z" fill="url(#flapLeft)"/>
      <path d="M170 191 C175 220 185 245 200 270 L212 270 C195 245 184 220 186 200 Z" fill="#e52833"/>
      <path d="M992 29 C1000 60 1010 90 1027 109 C1020 112 1012 108 1008 104 C998 80 993 55 992 29 Z" fill="url(#flapRight)"/>
      <path d="M1027 109 C960 150 920 220 883 270 L895 270 C930 220 970 160 1020 114 Z" fill="#e52833"/>
    </svg>

    <ul class="benefits">
      <li class="benefit" style="left:321px">
        <svg class="benefit__icon" viewBox="0 0 50 50" aria-hidden="true" fill="none" stroke="#fff" stroke-width="2.6" stroke-linecap="round">
          <circle cx="29" cy="27" r="15"/>
          <path d="M29 8 v4 M26 7 h6 M29 27 l6 -6"/>
          <path d="M4 20 h9 M2 25 h10 M4 30 h9 M6 35 h8"/>
        </svg>
        FREE SHIPPING<br>AUSTRALIA WIDE
      </li>
      <li class="benefit" style="left:438px">
        <svg class="benefit__icon" viewBox="0 0 50 50" aria-hidden="true" fill="none" stroke="#fff" stroke-width="2.6" stroke-linecap="round" stroke-linejoin="round">
          <rect x="4" y="8" width="32" height="30" rx="4"/>
          <path d="M4 16 h32 M12 4 v8 M28 4 v8"/>
          <path d="M10 22 h3 M17 22 h3 M24 22 h3 M10 28 h3 M17 28 h3 M10 33 h3"/>
          <circle cx="36" cy="36" r="11" fill="#d01c24"/>
          <text x="36" y="40" text-anchor="middle" font-family="Montserrat, sans-serif" font-size="10" font-weight="600" fill="#fff" stroke="none">24</text>
        </svg>
        SAME DAY<br>DISPATCH
      </li>
      <li class="benefit" style="left:544px">
        <svg class="benefit__icon" viewBox="0 0 50 50" aria-hidden="true" fill="none" stroke="#fff" stroke-width="2.4" stroke-linecap="round" stroke-linejoin="round">
          <circle cx="25" cy="20" r="16"/>
          <circle cx="25" cy="20" r="10"/>
          <path d="M16 34 l-5 12 l6 -3 l3 5 l4 -10 M34 34 l5 12 l-6 -3 l-3 5 l-4 -10"/>
          <text x="25" y="25" text-anchor="middle" font-family="Montserrat, sans-serif" font-size="13" font-weight="600" fill="#fff" stroke="none">$</text>
        </svg>
        BEST PRICE<br>GUARANTEE
      </li>
      <li class="benefit" style="left:650px">
        <svg class="benefit__icon" viewBox="0 0 50 50" aria-hidden="true">
          <circle cx="25" cy="25" r="20" fill="none" stroke="#fff" stroke-width="2.8"/>
          <path d="M7 32 h36 v4 h-36 z" fill="#fff"/>
          <text x="25" y="28" text-anchor="middle" font-family="Montserrat, sans-serif" font-size="20" font-weight="600" fill="#fff">5</text>
          <text x="25" y="35.5" text-anchor="middle" font-family="Montserrat, sans-serif" font-size="4.5" fill="#d01c24">★★★★★</text>
        </svg>
        3000+ 5 STAR<br>REVIEWS
      </li>
      <li class="benefit" style="left:758px">
        <svg class="benefit__icon" viewBox="0 0 50 50" aria-hidden="true" fill="none" stroke="#fff" stroke-linecap="round">
          <path d="M10 10 L40 40" stroke-width="5"/>
          <path d="M40 8 L12 36" stroke-width="4"/>
          <circle cx="10" cy="40" r="5" stroke-width="3"/>
          <path d="M36 5 a7 7 0 1 0 9 9" stroke-width="3"/>
        </svg>
        BEST SERVICE &amp;<br>WARRANTY
      </li>
      <li class="benefit" style="left:865px">
        <svg class="benefit__icon" viewBox="0 0 50 50" aria-hidden="true">
          <path d="M25 4 L42 10 V24 C42 35 34 42 25 46 C16 42 8 35 8 24 V10 Z" fill="none" stroke="#fff" stroke-width="3" stroke-linejoin="round"/>
          <rect x="18" y="22" width="14" height="11" rx="1.5" fill="#fff"/>
          <path d="M20.5 22 v-3 a4.5 4.5 0 0 1 9 0 v3" fill="none" stroke="#fff" stroke-width="2.4"/>
          <circle cx="25" cy="27" r="1.6" fill="#d01c24"/>
        </svg>
        100% SECURE<br>CHECKOUT
      </li>
    </ul>

    <a class="cart-button" href="https://www.brimlark.com.au/collections/gel-blasters" aria-label="Shop gel blasters" style="left:1046px;top:170px">
      <svg width="40" height="36" viewBox="0 0 40 36" aria-hidden="true" fill="none" stroke="var(--cart-red)" stroke-width="3.4" stroke-linecap="round" stroke-linejoin="round">
        <path d="M2 4 h6 l5 20 h20 l4 -16 h-26"/>
        <path d="M17 12 v8 M22 12 v8 M27 12 v8"/>
        <circle cx="15" cy="31" r="2.6"/>
        <circle cx="31" cy="31" r="2.6"/>
      </svg>
    </a>
  </section>
</body>
</html>
```